Tutoring Website Needs a Facelift

BrightStudyDesk.com needs a facelift! We are looking to completely redo our website, and logo to give it a more professional, cleaner, and younger vibe.
Our site feels out dated and not very Web 2.0
We are looking to keep the same content on the page now but completely rebrand it to give it the new look we desire.
Updates
Target Market(s)
College Students but needs to portray professionalism, and trust to them
Industry/Entity Type
Tutoring
Look and feel
Each slider illustrates characteristics of the customer's brand and the style your logo design should communicate.

```html
<!DOCTYPE html>
<html lang="en">
<head>
<meta charset="utf-8">
<title>BrightStudyDesk.com – Submission Form</title>
<link href="https://fonts.googleapis.com/css2?family=Open+Sans:wght@400;600&family=Sue+Ellen+Francisco&display=swap" rel="stylesheet">
<style>
:root{
  --page:#f4f5f6;
  --accent:#2f9bd6;
  --nav:#3d6e91;
  --nav-dark:#2b5473;
  --panel:#e9eaeb;
  --board:#3a3b3c;
  --board-frame:#cfd1d3;
  --personal:#98a3ac;
  --assignment:#a2adb6;
  --field:#ffffff;
  --label:#ffffff;
  --footer:#6a6e74;
  --footer-bar:#55585d;
  --green:#6cbf3a;
  --blue-btn:#4d9fd6;
  --logo:#3a4a5a;
}
*{margin:0;padding:0;box-sizing:border-box}
html,body{width:843px;height:1200px;overflow:hidden}
body{position:relative;background:var(--page);font-family:"Open Sans",sans-serif;color:var(--label)}
.abs{position:absolute}
.top-line{left:0;top:0;width:843px;height:4px;background:var(--accent)}
.brand{left:40px;top:36px;display:flex;align-items:center;gap:8px}
.brand-mark{width:18px;height:18px;border-radius:50%;background:#f0a51c}
.brand-name{font-size:19px;font-weight:400;color:var(--logo);letter-spacing:.5px}
.social{display:flex;gap:10px}
.social span{width:26px;height:26px;border-radius:5px;background:#7f8c98}
.social-top{left:661px;top:52px}
.flap{top:106px;width:30px;height:34px;background:var(--nav-dark)}
.nav{left:20px;top:91px;width:805px;height:35px;background:linear-gradient(#4a7ea3,var(--nav));display:flex;justify-content:space-around;align-items:center;padding:0 90px 0 80px}
.nav a{font-family:"Sue Ellen Francisco",cursive;color:#fff;text-decoration:none;font-size:15px}
.main{left:33px;top:126px;width:775px;height:930px;background:var(--panel)}
.board-frame{left:57px;top:136px;width:724px;height:247px;background:var(--board-frame)}
.board{left:62px;top:140px;width:715px;height:238px;background:radial-gradient(circle at 40% 40%,#4a4b4c,var(--board));border:2px solid #5b5c5d;padding:30px 38px;font-size:12px;line-height:15px}
.board h1{font-family:"Sue Ellen Francisco",cursive;font-weight:400;font-size:22px;line-height:22px;margin-bottom:22px}
.board p{margin-bottom:16px;max-width:600px;letter-spacing:.2px}
.board p.small{font-size:10.5px;line-height:14.5px;max-width:625px}
.sketch{left:600px;top:295px;width:140px;height:70px;background:linear-gradient(90deg,#4a4b4c,#5a5b5c);border-radius:4px;opacity:.6}
.section{left:33px;width:775px}
.personal{top:400px;height:260px;background:var(--personal)}
.assignment{top:660px;height:350px;background:var(--assignment)}
.dash{left:33px;width:775px;border-top:1.5px dashed #e6eaee}
h2.hand{position:absolute;font-family:"Sue Ellen Francisco",cursive;font-weight:400;font-size:20px;line-height:22px;color:#fff;padding-bottom:3px;border-bottom:1px dashed #c5ccd2;width:200px}
.label{position:absolute;font-size:12.5px;line-height:16px}
.hint{position:absolute;font-size:7.5px;line-height:10px;color:#dfe3e6}
.edu{position:absolute;font-size:9.5px;color:#c81e1e;text-decoration:line-through}
.field{position:absolute;background:var(--field);border-radius:4px;box-shadow:0 0 0 3px rgba(140,150,159,.45)}
.select{position:absolute;background:var(--field);border-radius:4px;box-shadow:0 0 0 3px rgba(140,150,159,.45);color:#b5bcc2;font-size:12px;padding-left:9px;display:flex;align-items:center}
.select i{position:absolute;right:3px;top:3px;bottom:3px;width:22px;border-radius:3px;background:linear-gradient(#6e9cbd,#4b7b9e)}
.select i svg{display:block;margin:7px auto 0}
.sm{font-size:10px;padding-left:7px}
.illustration{left:430px;top:453px;width:314px;height:179px;background:linear-gradient(135deg,#c9343a 0%,#e8e3dc 45%,#e8b43a 100%);border-radius:6px;opacity:.85}
.btn-file{left:412px;top:744px;width:100px;height:23px;border-radius:4px;background:linear-gradient(#62b0e4,var(--blue-btn));font-size:10.5px;display:flex;align-items:center;justify-content:center}
.submit{left:412px;top:927px;width:130px;height:23px;border-radius:3px;background:linear-gradient(#80d04a,var(--green));font-size:12.5px;display:flex;align-items:center;justify-content:center}
.footer{left:0;top:1056px;width:843px;height:111px;background:var(--footer)}
.footer-bar{left:0;top:1167px;width:843px;height:33px;background:var(--footer-bar);font-size:7px;color:#eef}
.footer-text{left:74px;top:1085px;font-size:7.8px;line-height:10.3px;color:#eceef0}
.badge{left:366px;top:1019px;width:128px;height:128px;border-radius:50%;background:radial-gradient(circle,#e2c074 0 45%,#2a2a2a 46% 100%)}
.brand-foot{left:560px;top:1090px}
.social-foot{left:620px;top:1128px}
</style>
</head>
<body>
<div class="abs top-line"></div>
<div class="abs brand"><span class="brand-mark"></span><span class="brand-name">BRIGHTSTUDYDESK</span></div>
<div class="abs social social-top" aria-label="Social links"><span></span><span></span><span></span><span></span></div>

<div class="abs flap" style="left:0"></div>
<div class="abs flap" style="left:813px"></div>
<nav class="abs nav"><a href="#">Home</a><a href="#">Submission Form</a><a href="#">Testimonials</a><a href="#">FAQ</a><a href="#">Contact us</a></nav>

<div class="abs main"></div>
<div class="abs board-frame"></div>
<section class="abs board">
  <h1>Submission Form</h1>
  <p>Please complete this form with as much detail as possible. You will be notified via email within 30 minutes if your "work" has been accepted.</p>
  <p class="small">&nbsp;If accepted an e-mail will be sent to you that will contain an invoice. This invoice needs to be paid within 24 hours. No assignment will be started without a fully paid invoice. On your credit card statement, your paid invoice will appear as "NORTHGATE STUDY SERVICES".your life.</p>
</section>
<div class="abs sketch" role="img" aria-label="Chalk sketch of an arrow pointing to a notepad"></div>

<div class="abs section personal"></div>
<div class="abs section assignment"></div>
<div class="abs dash" style="top:407px"></div>
<div class="abs dash" style="top:1002px"></div>

<h2 class="hand" style="left:103px;top:428px">Personal Information</h2>
<span class="label" style="left:110px;top:467px">Name:</span>
<div class="field" style="left:110px;top:496px;width:201px;height:26px"></div>
<span class="label" style="left:110px;top:552px">Email:</span>
<span class="edu" style="left:111px;top:565px">.edu</span>
<span class="hint" style="left:111px;top:578px">(for your safety and privacy .edu email addresses<br>are not allowed, please use your personal email address)</span>
<div class="field" style="left:110px;top:603px;width:201px;height:27px"></div>
<div class="abs illustration" role="img" aria-label="Illustration of an open red notebook with pen, ruler and set square"></div>

<h2 class="hand" style="left:106px;top:680px">Assignment Information</h2>
<span class="label" style="left:110px;top:716px">What Class for?</span>
<div class="select" style="left:110px;top:742px;width:201px;height:27px">Please Select<i><svg width="10" height="7"><path d="M1 1l4 4 4-4" stroke="#fff" stroke-width="2" fill="none"/></svg></i></div>
<span class="label" style="left:109px;top:786px">What type of assignment?</span>
<div class="select" style="left:110px;top:810px;width:201px;height:26px">Please Select<i><svg width="10" height="7"><path d="M1 1l4 4 4-4" stroke="#fff" stroke-width="2" fill="none"/></svg></i></div>
<span class="label" style="left:110px;top:851px;font-size:11px;line-height:13px">Please explain the assignment with as much<br>detail as possible:</span>
<div class="field" style="left:110px;top:888px;width:258px;height:96px;border-radius:8px"></div>

<span class="label" style="left:408px;top:716px">Please attach any files that we may need:</span>
<div class="abs btn-file">choose file</div>
<span class="label" style="left:522px;top:748px;font-size:10.5px;color:#3b4650">no file chosen</span>
<span class="label" style="left:411px;top:788px;font-size:11px">When do you need this assignment emailed to you by? <span style="color:#2d6e9c">(EST)</span></span>
<div class="select sm" style="left:413px;top:811px;width:80px;height:26px">Month<i><svg width="10" height="7"><path d="M1 1l4 4 4-4" stroke="#fff" stroke-width="2" fill="none"/></svg></i></div>
<div class="select sm" style="left:504px;top:811px;width:66px;height:26px">Day<i><svg width="10" height="7"><path d="M1 1l4 4 4-4" stroke="#fff" stroke-width="2" fill="none"/></svg></i></div>
<div class="select sm" style="left:583px;top:811px;width:67px;height:26px">Time<i><svg width="10" height="7"><path d="M1 1l4 4 4-4" stroke="#fff" stroke-width="2" fill="none"/></svg></i></div>
<div class="select sm" style="left:663px;top:811px;width:56px;height:26px">AM<i><svg width="10" height="7"><path d="M1 1l4 4 4-4" stroke="#fff" stroke-width="2" fill="none"/></svg></i></div>
<span class="label" style="left:412px;top:856px">How much were you hoping to pay for this assignment?</span>
<div class="select" style="left:412px;top:889px;width:128px;height:27px;font-size:12px">Name your price</div>
<div class="abs submit">Submit</div>

<footer>
  <div class="abs footer"></div>
  <p class="abs footer-text">All assignments are originally created for you. We will<br>never share your work<br>with another student nor plagiarize any source.<br><br>Privacy. After submission your work takes on its own<br>identity and your name<br>is never associated with it.</p>
  <div class="abs badge" role="img" aria-label="Satisfaction guarantee seal"></div>
  <div class="abs brand brand-foot"><span class="brand-mark"></span><span class="brand-name" style="color:#fff">BRIGHTSTUDYDESK</span></div>
  <div class="abs social social-foot" aria-label="Social links"><span></span><span></span><span></span><span></span></div>
  <div class="abs footer-bar">
    <span class="abs" style="left:74px;top:12px">Copyright © 2010 BrightStudyDesk.com. All rights reserved.</span>
    <span class="abs" style="left:333px;top:12px">BrightStudyDesk.com is a tutoring service. You decide how to use our service within the guidelines of your high school, college or university.</span>
  </div>
</footer>
</body>
</html>
```